Global Nano Technology Surface Protection company needs a new logo and cards

We are a Global company that will apply nanotechnology coatings on surfaces to prevent growth and spread of bacteria, viruses, mold etc. We deal with large corporates, airlines, hospitals and schools so we are after a new modern, simple and clean look that will have great visual impact.
We a company that is focused on prevention and protection.

Company name, Quorvane Systems Worldwide

Subtext, Antimicrobial Surface Protection

Logo, QVSW or QSW

Target Market(s)

Hospitals, Transport agencies, Airlines, Corporate entities

Industry/Entity Type

Protection

Contact Information for Business Card

Logo, QVSW or QSW
www.qvsw-example.us
Derek Holloway
+64290536218
tidyshieldnz@mailbox-example.com

Logo Text

QVSW

Requirements
Must have
• Simple clean look
Should not have
• Nothing too messy

```html
<!DOCTYPE html>
<html lang="en">
<head>
<meta charset="utf-8">
<title>Quorvane Systems Worldwide — Business Card</title>
<link rel="stylesheet" href="https://fonts.googleapis.com/css2?family=Poppins:wght@400;600&family=Raleway:wght@500;700&display=swap">
<style>
  :root {
    --brand-red: #ed1c24;
    --ink-grey: #5a5a5a;
    --text-grey: #444444;
    --card-white: #ffffff;
    --backdrop: #e4e6e8;
  }
  * { box-sizing: border-box; margin: 0; padding: 0; }
  html, body {
    width: 1200px;
    height: 854px;
    overflow: hidden;
    background: var(--backdrop);
  }
  .stage {
    width: 1200px;
    height: 854px;
    display: flex;
    align-items: center;
    justify-content: center;
    gap: 40px;
  }
  .card {
    width: 520px;
    height: 300px;
    position: relative;
    box-shadow: 0 6px 18px rgba(0,0,0,0.12);
  }
  .card-front {
    background: var(--brand-red);
    display: flex;
    align-items: center;
    justify-content: center;
  }
  .wordmark {
    display: flex;
    align-items: center;
    gap: 12px;
    font-family: "Raleway", sans-serif;
    font-weight: 700;
    letter-spacing: 2px;
  }
  .wordmark-square {
    display: block;
    background: currentColor;
  }
  .card-front .wordmark {
    color: var(--card-white);
    font-size: 50px;
  }
  .card-front .wordmark-square { width: 22px; height: 22px; }

  .card-back {
    background: var(--card-white);
  }
  .contact-block {
    position: absolute;
    left: 34px;
    top: 38px;
  }
  .person-name {
    font-family: "Poppins", sans-serif;
    font-weight: 600;
    font-size: 19px;
    letter-spacing: 0.5px;
    text-transform: uppercase;
    color: var(--ink-grey);
    margin-bottom: 8px;
  }
  .contact-list { list-style: none; }
  .contact-item {
    display: flex;
    align-items: center;
    gap: 8px;
    font-family: "Poppins", sans-serif;
    font-size: 12.5px;
    color: var(--text-grey);
    line-height: 21px;
  }
  .contact-icon { width: 13px; height: 13px; flex: none; }

  .brand-block {
    position: absolute;
    right: 34px;
    bottom: 30px;
    width: 270px;
    display: flex;
    flex-direction: column;
    align-items: center;
    text-align: center;
  }
  .card-back .wordmark {
    color: var(--brand-red);
    font-size: 30px;
    margin-bottom: 14px;
  }
  .card-back .wordmark-square { width: 13px; height: 13px; }
  .company-name {
    font-family: "Raleway", sans-serif;
    font-weight: 500;
    font-size: 21px;
    line-height: 25px;
    color: var(--ink-grey);
  }
  .company-tagline {
    margin-top: 9px;
    font-family: "Poppins", sans-serif;
    font-size: 9px;
    letter-spacing: 0.6px;
    text-transform: uppercase;
    color: var(--text-grey);
    align-self: flex-end;
  }
</style>
</head>
<body>
  <main class="stage">
    <section class="card card-front" aria-label="Card front">
      <div class="wordmark"><span class="wordmark-square"></span>QVSW</div>
    </section>

    <section class="card card-back" aria-label="Card back">
      <div class="contact-block">
        <h1 class="person-name">Derek Holloway</h1>
        <ul class="contact-list">
          <li class="contact-item">
            <svg class="contact-icon" viewBox="0 0 14 14" aria-hidden="true">
              <circle cx="7" cy="7" r="7" fill="var(--brand-red)"/>
              <path d="M4.6 3.6l1.3 1.3-.7 1c.5 1 1.3 1.8 2.3 2.3l1-.7 1.3 1.3-.9 1.1C6.6 9.7 4.3 7.4 3.5 4.5z" fill="#fff"/>
            </svg>
            +64290536218
          </li>
          <li class="contact-item">
            <svg class="contact-icon" viewBox="0 0 14 14" aria-hidden="true">
              <circle cx="7" cy="7" r="7" fill="var(--brand-red)"/>
              <circle cx="7" cy="7" r="1.6" fill="none" stroke="#fff" stroke-width="1.1"/>
              <path d="M8.6 5.6v2.2c0 .9 1.6.9 1.6-.6A3.2 3.2 0 1 0 8.8 9.8" fill="none" stroke="#fff" stroke-width="1.1"/>
            </svg>
            tidyshieldnz@mailbox-example.com
          </li>
          <li class="contact-item">
            <svg class="contact-icon" viewBox="0 0 14 14" aria-hidden="true">
              <circle cx="7" cy="7" r="7" fill="var(--brand-red)"/>
              <circle cx="7" cy="7" r="4" fill="none" stroke="#fff" stroke-width="0.9"/>
              <ellipse cx="7" cy="7" rx="1.7" ry="4" fill="none" stroke="#fff" stroke-width="0.9"/>
              <path d="M3 7h8" stroke="#fff" stroke-width="0.9"/>
            </svg>
            www.qvsw-example.com
          </li>
        </ul>
      </div>

      <div class="brand-block">
        <div class="wordmark"><span class="wordmark-square"></span>QVSW</div>
        <p class="company-name">Quorvane Systems<br>Worldwide</p>
        <p class="company-tagline">Antimicrobial Surface Protection</p>
      </div>
    </section>
  </main>
</body>
</html>
```